Build PowerPoint for New Logo & Letterhead

I have started my own consulting firm and created a logo and letterhead (attached) am looking PowerPoint template. My name is Dorrit Okonkwo-Haverly and the company is called Birchpoint Consulting. We primarily use PowerPoint files to display analyses, maps and key talking points from interviews and/or recommendations. We use the documents more to facilitate discussion with our target audiences. Most of the time our PowerPoint document is printed as handouts for our clients and not projected.

Target Market(s)

Healthcare provider organizations (hospitals, health systems, physician groups)

Industry/Entity Type

Healthcare

Font styles to use
Sans Serif

Colors
abd036
1f9ad1
0355a3

Requirements
Must have
• I would like to cover page to play off of the letterhead in some fashion. I want the design to provide plenty of space for text, graphics, maps, pictures, etc.
• We will usually include our clients logo somewhere on the document. Historically it is prominent on the cover page and then in one of the corners on all of the pages thereafter.

```html
<!DOCTYPE html>
<html lang="en">
<head>
<meta charset="utf-8">
<title>Birchpoint Consulting – Cover Slide</title>
<link rel="stylesheet" href="https://fonts.googleapis.com/css2?family=Saira:wght@500;600&display=swap">
<style>
  :root {
    --sky-top: #03abf6;
    --sky-bottom: #1b7dbf;
    --leaf-green: #9ecd3a;
    --brand-blue: #1f9ad1;
    --paper: #ffffff;
    --ink-grey: #5b6168;
    --title-white: #ffffff;
  }
  * { margin: 0; padding: 0; box-sizing: border-box; }
  html, body {
    width: 1200px;
    height: 900px;
    overflow: hidden;
    background: var(--paper);
  }
  .slide {
    position: relative;
    width: 1200px;
    height: 900px;
    background: var(--paper);
    font-family: "Saira", "Arial", sans-serif;
  }
  .hero {
    position: absolute;
    left: 0; top: 0;
    width: 1200px;
    height: 590px;
    background: linear-gradient(180deg, var(--sky-top) 0%, var(--sky-bottom) 100%);
  }
  .hero-rule {
    position: absolute;
    left: 0; top: 590px;
    width: 1200px;
    height: 8px;
    background: var(--leaf-green);
  }
  .title-block {
    position: absolute;
    left: 0; top: 270px;
    width: 1195px;
    text-align: center;
    color: var(--title-white);
  }
  .project-title {
    font-size: 48px;
    font-weight: 500;
    letter-spacing: 1.5px;
    line-height: 1;
  }
  .project-subtitle {
    margin-top: 22px;
    font-size: 20px;
    font-weight: 600;
    letter-spacing: 1.5px;
    line-height: 1;
  }
  .firm-mark {
    position: absolute;
    right: 38px;
    top: 660px;
    display: flex;
    flex-direction: column;
    align-items: flex-end;
    gap: 18px;
  }
  .firm-square {
    width: 82px;
    height: 82px;
    background: var(--brand-blue);
  }
  .firm-name {
    font-size: 19px;
    font-weight: 500;
    letter-spacing: 4px;
    color: var(--ink-grey);
    text-align: right;
    line-height: 1.3;
  }
  .footer-band {
    position: absolute;
    left: 0; bottom: 0;
    width: 1200px;
    height: 57px;
  }
</style>
</head>
<body>
  <main class="slide">
    <section class="hero">
      <div class="title-block">
        <h1 class="project-title">PROJECT TITLE HERE</h1>
        <p class="project-subtitle">SUBTEXT HERE</p>
      </div>
    </section>
    <div class="hero-rule"></div>

    <div class="firm-mark">
      <div class="firm-square"></div>
      <p class="firm-name">BIRCHPOINT<br>CONSULTING</p>
    </div>

    <svg class="footer-band" viewBox="0 0 1200 57" aria-hidden="true">
      <polygon points="0,0 248,0 270,27 1200,27 1200,57 0,57" fill="var(--leaf-green)"/>
    </svg>
  </main>
</body>
</html>
```